Printed Promo Flyer for new pet business

We need a double sided flyer design as per the given example flyer, just better looking and more fun.Flyers will need to be printed.Flyer size approx 10.5cm x 15cm. The text will need to be amended slightly afterwards to be more fun unless you can create a new tone of voice as well (should sound fun like breezy do it) Look and Feel: emotional, fun, loving, professional
See attached files.

Target Market(s)

Pet owners in the UK who want the convenience of getting their pets parasite treatment delivered to their door without the need of having to run to the vet or store for purchase

Industry/Entity Type

Pet Care

Colors
00a990
6b449b

Requirements
Must have
• all the content context as given in the example flyer.
Nice to have
• Tone of voice can be changed to be more fun (using Breezy as a guide)

```html
<!DOCTYPE html>
<html lang="en">
<head>
<meta charset="utf-8">
<title>Pawtuck Box – Promo Flyer</title>
<link rel="stylesheet" href="https://fonts.googleapis.com/css2?family=Bebas+Neue&family=Lato:wght@400;700&family=Oswald:wght@500&display=swap">
<style>
  :root {
    --teal: #00a990;
    --purple: #6b449b;
    --white: #ffffff;
    --ink: #111111;
    --stage: #2d2d2d;
    --photo-warm: #c9a27a;
    --photo-cool: #b9b7bd;
  }
  * { box-sizing: border-box; margin: 0; padding: 0; }
  html, body { width: 1200px; height: 1200px; overflow: hidden; background: var(--stage); }
  .flyer {
    position: absolute; left: 264px; top: 148px; width: 672px; height: 962px;
    background: var(--white); overflow: hidden;
    font-family: "Lato", sans-serif; color: var(--ink);
  }
  .flyer-shapes { position: absolute; inset: 0; }
  .block { position: absolute; text-align: center; }
  .heading { font-family: "Bebas Neue", sans-serif; color: var(--teal); line-height: 1; }
  .why-title { left: 0; width: 332px; top: 204px; font-size: 40px; }
  .benefit-title { color: var(--purple); font-weight: 700; font-size: 17.5px; }
  .benefit-text { font-size: 17px; line-height: 1.05; }
  .brand { left: 340px; width: 312px; top: 200px; }
  .brand-name {
    font-family: "Lato", sans-serif; font-weight: 700; color: var(--purple);
    font-size: 31px; letter-spacing: 2px; display: inline-flex; align-items: center; gap: 10px;
  }
  .brand-dot { width: 13px; height: 13px; border-radius: 50%; background: var(--teal); display: inline-block; }
  .tagline { left: 340px; width: 312px; top: 286px; font-size: 42px; }
  .register { position: absolute; left: 24px; top: 608px; font-family: "Bebas Neue", sans-serif;
    color: var(--white); font-size: 24px; line-height: 0.95; }
  .how-title { left: 412px; width: 220px; top: 414px; font-family: "Bebas Neue", sans-serif;
    color: var(--white); font-size: 42px; }
  .steps { position: absolute; left: 390px; top: 470px; width: 280px; list-style: none; }
  .step { position: absolute; left: 0; display: flex; gap: 8px; align-items: center;
    color: var(--white); font-size: 19px; line-height: 1; }
  .step-num { flex: 0 0 30px; height: 30px; border-radius: 50%; background: var(--white);
    color: var(--purple); font-size: 17px; display: flex; align-items: center; justify-content: center; }
  .offer { left: 490px; width: 160px; top: 752px; color: var(--white); }
  .offer-title { font-family: "Bebas Neue", sans-serif; font-size: 40px; line-height: 1; }
  .offer-price { display: inline-block; background: var(--teal); font-family: "Bebas Neue", sans-serif;
    font-size: 54px; line-height: 1; padding: 2px 6px 0; margin-top: 2px; }
  .offer-code { font-family: "Lato", sans-serif; font-weight: 700; font-size: 20px; margin-top: 2px; letter-spacing: 1px; }
  .offer-code-box { display: inline-block; width: 80px; background: #2a2a2a; font-family: "Oswald", sans-serif;
    font-size: 14px; letter-spacing: 6px; line-height: 16px; }
  .site { left: 0; width: 672px; top: 918px; font-family: "Oswald", sans-serif; color: var(--white);
    font-size: 20px; letter-spacing: 4px; }
</style>
</head>
<body>
<main class="flyer">
  <svg class="flyer-shapes" width="672" height="962" viewBox="0 0 672 962">
    <path fill="var(--purple)" d="M250,0 H672 V250 C620,180 540,120 440,140 C410,146 380,160 350,180 C340,100 300,40 250,0 Z"/>
    <path fill="var(--teal)" d="M0,0 H270 C360,30 380,150 340,205 C300,230 260,170 200,120 C150,70 60,45 0,40 Z"/>
    <path fill="var(--purple)" d="M330,398 C360,392 390,394 412,398 L360,570 C320,565 260,550 210,566 C270,500 318,460 330,398 Z"/>
    <path fill="var(--teal)" d="M412,398 H628 L672,468 V700 L630,760 L340,760 L300,640 L345,565 Z"/>
    <path fill="var(--teal)" d="M0,580 C120,560 230,540 300,556 L340,650 C250,650 100,668 0,692 Z"/>
    <path fill="var(--purple)" d="M430,760 C500,722 600,702 672,740 V914 H440 C418,870 418,800 430,760 Z"/>
    <rect fill="var(--teal)" x="0" y="914" width="672" height="48"/>

    <path role="img" aria-label="Photo: golden retriever cuddling a grey cat" fill="var(--photo-warm)" stroke="var(--purple)" stroke-width="2"
      d="M60,60 C80,10 150,0 200,30 C240,55 270,90 252,120 C230,150 190,150 150,170 C110,190 70,190 56,150 C48,120 50,90 60,60 Z"/>
    <path role="img" aria-label="Photo: small dog and cat under a blanket" fill="var(--photo-cool)"
      d="M560,20 C590,0 640,0 672,10 V150 C630,158 590,150 560,140 C530,120 530,70 560,20 Z"/>
    <path role="img" aria-label="Photo: tabby cat lying on a white bed" fill="#bfae98" stroke="var(--teal)" stroke-width="2"
      d="M170,560 C190,530 230,520 260,540 C300,565 340,590 356,620 C366,660 330,700 290,712 C240,722 190,700 172,660 C158,620 158,590 170,560 Z"/>
    <path role="img" aria-label="Photo: French bulldog resting on a cushion" fill="#a89a8c" stroke="var(--purple)" stroke-width="2"
      transform="translate(-4,18)"
      d="M336,700 C360,680 400,686 430,710 C470,740 500,780 490,820 C478,860 430,878 390,870 C350,862 326,830 322,790 C318,750 320,715 336,700 Z"/>

    <g fill="var(--purple)">
      <circle cx="156" cy="282" r="26"/><circle cx="156" cy="426" r="26"/>
      <circle cx="156" cy="718" r="26"/><circle cx="156" cy="820" r="26"/>
    </g>
    <g fill="none" stroke="var(--white)" stroke-width="2.5" stroke-linecap="round" stroke-linejoin="round">
      <rect x="145" y="280" width="22" height="15" rx="2"/><path d="M149,280 V273 a7,7 0 0 1 14,0 V280"/>
      <circle cx="156" cy="426" r="14"/><path d="M156,417 V427 L162,431"/>
      <circle cx="156" cy="718" r="14"/><path d="M149,718 L154,723 L164,711"/>
      <circle cx="156" cy="820" r="14"/>
    </g>
    <text x="156" y="828" text-anchor="middle" fill="var(--white)" font-family="Lato, sans-serif" font-size="20">$</text>
  </svg>

  <h2 class="block heading why-title">Why Pawtuck Box ?</h2>

  <div class="block" style="left:0;width:312px;top:312px">
    <p class="benefit-title">Protection &amp; Care</p>
    <p class="benefit-text" style="margin-top:6px">Protection against all major parasites<br>to avoid putting your pet &amp; your<br>family at risk</p>
  </div>
  <div class="block" style="left:0;width:312px;top:458px">
    <p class="benefit-title">In Time</p>
    <p class="benefit-text" style="margin-top:4px">Never having to remember<br>when to treat your pet</p>
  </div>
  <p class="register">Register, choose<br>&amp; wait.</p>
  <div class="block" style="left:0;width:334px;top:748px">
    <p class="benefit-title">Convenient</p>
    <p class="benefit-text" style="margin-top:4px">Delivered directly to your letter box</p>
  </div>
  <div class="block" style="left:0;width:350px;top:852px">
    <p class="benefit-title">Low Cost</p>
    <p class="benefit-text" style="margin-top:4px">All the high end, trusted brands<br>but cheaper than the vet</p>
  </div>

  <div class="block brand"><span class="brand-name"><span class="brand-dot"></span>PAWTUCK BOX</span></div>
  <h1 class="block heading tagline">The best protection<br>for your pet</h1>

  <h2 class="block how-title">How it works</h2>
  <ol class="steps">
    <li class="step" style="top:0">    <span class="step-num">1.</span><span>Select which pet the<br>treatment is for</span></li>
    <li class="step" style="top:62px"> <span class="step-num">2.</span><span>Choose your treatment<br>type</span></li>
    <li class="step" style="top:128px"><span class="step-num">3.</span><span>Select your preferred<br>brand</span></li>
    <li class="step" style="top:184px"><span class="step-num">4.</span><span>Choose between 1,3,6 or<br>12 months treatment box</span></li>
  </ol>

  <div class="block offer">
    <p class="offer-title">First box</p>
    <p class="offer-price">$5.99</p>
    <p class="offer-code">Use Code</p>
    <p class="offer-code-box">XXX</p>
  </div>

  <p class="block site">PAWTUCKBOX.CO.UK</p>
</main>
</body>
</html>
```